Yoga Studio needs a new website

I am looking for someone to design a landing/home page for my website. The website will be developed using Wordpress, so please make sure your designs are compatible.

Please note the following design guidelines about the page:
1. The website is for a yoga studio called “Mirel Yoga”. The logo for our studio has been uploaded on along with this project. Mirel in Sanskrit means Truth and Yoga means unity or unification (with supreme consciousness).
2. The Yoga studio will probably the first of its kinda to offer true, authentic, spiritual experience to students in South Africa. More than that, it aims to setup itself as a hub for spiritualists and seekers irrespective of beliefs, religion and what philosophies they subscribe to.
3. Unlike modern schools, this school focuses on true elements of yoga - and teaches Yoga the way it was meant to be - no westernisation. Must have a peaceful, clam, very clean and spiritual look.
4. Please pay careful attention to the logo, color schemes and the simple design. The site must reflect exactly the same principles.
5. Please use the latest web design trends and ideas in your design. You are free to be as creative as you want.
6. You are free to combine or use design concepts from other philosophies such as Sufism, Bahai, Tantra, Buddhism etc. as long as it gels well with the Yoga theme.
7. The overall site should give a very sensual, feminine and very mystic feel.

Functionality, features and guidelines for the main page design:
1. The main page should give a very clean, expansive, clutter free look.
2. The designer should find a clean way to fit all the following links/information into a main page. First prize if the designer could fit everything in a “single screen” - no scrolling.
3. Visually, the following information must be presented on the main page:
1. The name/logo of the studio.
2. The following sections of the website should have a link on the main page. Sub items represent sub sections within a section.
1. Home - Redirects the user back to home page
2. About
1. Mirel Yoga
2. Instructors
3. FAQ
3. Private Sessions
4. Corporate
1. At Workplace
2. Offisite & Team Building
3. Specialized
5. Retreats
6. Therapy
1. Stress & Anxiety
2. Lifestyle Diseases
3. Rehabilitation
4. Others
7. Gallery
8. Contact Us
3. A Calendar for classes and events
4. A section to display latest blog articles with option to share on social media sites.
5. A separate section to display latest news items.
6. A section for photo gallery - the gallery can be categorised in albums. The main page can display a limited number of images and clicking on the image should take user to our flicker account.
7. Lastly, a nice and clean way to show our activity on various social media streams such as facebook, twitter, flickr, Facebook page, google plus etc.

Please do not limit yourself to the brief above. If you any creative ideas or concepts, please feel free to experiment and suggest new features. Use you full creativity.
Updates

Hi, Thank you for all the designs so far and for your hard work. Just wanted to let you know that you can also include design elements from other philosophies as well if you want to such as Sufism, Bahai, Tantra, Buddhism etc. as long as it gels well with the over all Yoga theme. Please also note that the final design have a mystic, feminine and sensual feel to it. Please also try and include/match the logo styles in the design as well. The site should look very premium, very exclusive - just like the logo.

Target Market(s)

the site is being designed for serious yoga practitioners and learners in the age group of 18-45

Industry/Entity Type

School

Requirements
Must have
• clean, expansive, elegant, simple, calming, soothing, peaceful

```html
<!DOCTYPE html>
<html lang="en">
<head>
<meta charset="utf-8">
<title>Mirel Yoga – Home</title>
<link rel="stylesheet" href="https://fonts.googleapis.com/css2?family=Lato:wght@400;700&family=Montserrat:wght@400;700&family=Roboto+Condensed:wght@400;700&display=swap">
<style>
:root{
  --blue:#1f3f9a;
  --royal:#2a4fb0;
  --navy:#14225a;
  --sky:#3b8fdc;
  --pale:#e6ebf8;
  --paper:#f4f6fc;
  --ink:#1a1a1a;
  --muted:#555;
  --nav-grey:#d9d9d9;
}
*{box-sizing:border-box;margin:0;padding:0}
html,body{width:760px;height:1200px;overflow:hidden}
body{position:relative;background:var(--paper);font-family:"Lato",sans-serif;color:var(--ink)}
.abs{position:absolute}

/* top navigation */
.top-nav{left:0;top:0;width:760px;height:30px;background:linear-gradient(#e6e6e6,var(--nav-grey));display:flex;justify-content:space-between;align-items:center;padding:0 25px 0 36px;font-family:"Roboto Condensed",sans-serif;font-size:12.5px;color:#333;z-index:3}

/* hero */
.hero{left:0;top:30px;width:760px;height:330px;background:linear-gradient(180deg,#c9d3de 0%,#dfe3e8 45%,#e9e2d8 75%,#d9cfc2 100%)}
.hero-photo{left:230px;top:0;width:530px;height:300px;background:radial-gradient(ellipse at 40% 50%,rgba(196,160,130,.55),transparent 60%),radial-gradient(ellipse at 80% 55%,rgba(210,190,175,.55),transparent 55%)}
.phone{right:36px;top:10px;display:flex;align-items:center;gap:6px;font-family:"Roboto Condensed",sans-serif;font-size:14px;color:#111}
.brand{left:48px;top:120px;display:flex;align-items:center;gap:12px}
.brand-dot{width:46px;height:46px;border-radius:50%;background:var(--blue)}
.brand-name{font-family:"Lato",sans-serif;font-weight:700;font-size:40px;color:var(--blue);letter-spacing:1px}
.brand-tag{left:92px;top:232px;font-family:"Lato",sans-serif;font-size:15px;letter-spacing:2px;color:#444}
.hero-band{left:0;top:266px;width:760px;height:64px;background:linear-gradient(90deg,rgba(255,255,255,.55),rgba(255,255,255,.2))}
.hero-line1{left:39px;top:270px;font-family:"Roboto Condensed",sans-serif;font-weight:700;font-size:22px;color:var(--blue)}
.hero-line2{left:39px;top:300px;font-family:"Roboto Condensed",sans-serif;font-weight:700;font-size:17px;color:var(--blue)}
.btn-start{left:614px;top:284px;width:102px;height:29px;border-radius:8px;background:linear-gradient(#3a78d6,#1b4aa8);color:#fff;font-family:"Roboto Condensed",sans-serif;font-weight:700;font-size:17px;display:flex;align-items:center;justify-content:center;box-shadow:0 1px 3px rgba(0,0,0,.3)}
.hero-arrow{top:150px}

/* welcome */
.welcome{left:0;top:360px;width:760px;height:281px;background:linear-gradient(180deg,#e9e3ef 0%,#f1e6ee 45%,#e5e6f1 100%)}
.welcome-title{left:35px;top:50px;display:flex;align-items:baseline;gap:8px}
.welcome-title .lead{font-family:"Montserrat",sans-serif;font-weight:700;font-size:23px;color:#111}
.welcome-title .name{font-family:"Lato",sans-serif;font-weight:700;font-size:26px;color:var(--blue)}
.welcome-rule{left:35px;top:85px;width:320px;height:1px;background:#bbb}
.welcome-copy{left:35px;top:100px;width:408px;font-size:8.6px;line-height:13.1px;color:#222}
.btn-more{left:35px;top:210px;width:88px;height:22px;background:var(--navy);color:#fff;font-family:"Roboto Condensed",sans-serif;font-size:10px;display:flex;align-items:center;padding-left:28px}
.btn-more .plus{position:absolute;left:-2px;top:4px;width:22px;height:22px;border-radius:50%;background:var(--navy);border:2px solid #fff;color:#fff;font-size:17px;line-height:17px;text-align:center}
.video{left:469px;top:56px;width:253px;height:156px;border:2px solid #fff;box-shadow:0 1px 4px rgba(0,0,0,.3);background:#999}
.video-frame{width:100%;height:134px;background:linear-gradient(160deg,#8c959e,#a99287 55%,#c07740)}
.video-bar{height:18px;background:#1b1b1b;display:flex;align-items:center;gap:6px;padding:0 6px;color:#fff;font-size:8px}
.video-track{flex:1;height:5px;border-radius:3px;background:#666;position:relative}
.video-track span{position:absolute;left:36%;top:-2px;width:9px;height:9px;border-radius:50%;background:#ccc}
.video-note{left:484px;top:222px;display:flex;align-items:center;gap:8px;font-family:"Montserrat",sans-serif;font-size:11px;color:var(--blue);letter-spacing:.3px}

/* cards */
.card{top:662px;height:215px;background:var(--pale);border:1px solid #d3dbef}
.card-tab{position:absolute;left:20px;top:0;height:46px;right:-6px;background:#fff;box-shadow:3px 3px 4px rgba(0,0,0,.2);display:flex;align-items:center;padding-left:14px;font-family:"Montserrat",sans-serif;font-weight:700;font-size:12.5px;color:#111}
.card-tab b{color:var(--sky);font-weight:400;margin-left:4px}
.card-tab .leaf{position:absolute;right:18px;top:4px}
.blog-card{left:35px;width:231px}
.news-card{left:289px;width:199px}
.event-card{left:498px;width:227px}
.post{position:absolute;font-size:9px}
.post .t{color:var(--navy);font-weight:700;text-decoration:underline;font-size:9.5px}
.post .d{color:var(--sky);font-size:8.5px;margin:6px 0 5px}
.post .x{font-weight:700;font-size:9px;line-height:12px}
.post .x em{font-style:normal;color:var(--blue)}
.share{display:flex;gap:3px;margin-top:3px}
.share span{font-size:6.5px;padding:1px 4px;border:1px solid #bbb;background:#fff;color:#333}
.share span:first-child{background:#4a62a8;color:#fff;border-color:#4a62a8}
.thumb{position:absolute;background:linear-gradient(135deg,#6a4a3a,#b08968 55%,#d9c1a4)}
.pager{position:absolute;right:6px;bottom:6px;width:18px;height:18px;border-radius:50%;background:#fff;font-size:9px;text-align:center;line-height:17px;color:#333;box-shadow:0 0 2px rgba(0,0,0,.3)}
.news-item{position:absolute;left:0;display:flex;gap:8px}
.news-date{width:36px;text-align:center}
.news-date .n{background:var(--navy);color:#fff;font-family:"Montserrat",sans-serif;font-weight:700;font-size:14px;height:20px;line-height:20px}
.news-date .m{background:#fff;font-size:8.5px;height:16px;line-height:16px;border-bottom:2px solid var(--navy)}
.news-text{font-size:8.6px;line-height:12px;color:#333;width:150px}
.news-text strong{display:block;color:#111;font-size:9px;margin-bottom:2px}
.cal{position:absolute;left:35px;top:57px;width:160px;background:var(--royal);color:#fff}
.cal-head{display:flex;justify-content:space-between;padding:6px 8px;background:var(--navy);font-family:"Montserrat",sans-serif;font-size:10px}
.cal-grid{display:grid;grid-template-columns:repeat(7,1fr);padding:4px 4px 6px;row-gap:5px;font-size:9px;text-align:center}
.cal-grid .w{font-weight:700}
.cal-grid .today{outline:1px solid #fff;outline-offset:-1px;margin:0 4px}
.cal-note{position:absolute;left:0;width:100%;top:196px;text-align:center;font-size:9px;color:#444}

/* gallery */
.gallery-title{left:37px;top:915px;font-family:"Montserrat",sans-serif;font-weight:700;font-size:13px}
.gallery-title b{color:var(--sky);font-weight:400}
.film{left:35px;top:944px;width:690px;height:157px;background:var(--navy)}
.film-holes{position:absolute;left:8px;right:8px;height:9px;display:flex;justify-content:space-between}
.film-holes i{width:9px;height:9px;background:#fff;border-radius:2px}
.film-photo{position:absolute;top:21px;width:133px;height:111px;border:2px solid #fff}
.film-arrow{position:absolute;top:67px;width:19px;height:19px;border-radius:50%;background:#5a86d6;border:1px solid #fff}

/* social rail */
.social{left:733px;top:1039px;width:27px;height:89px;background:#4d77c9;display:flex;flex-direction:column;align-items:center;justify-content:space-evenly}
.social i{width:13px;height:13px;border-radius:50%;background:#fff}

/* footer */
.foot-nav{left:0;top:1131px;width:760px;height:43px;background:linear-gradient(var(--royal),var(--blue));display:flex;justify-content:center;align-items:center}
.foot-nav ul{list-style:none;display:flex;border-top:1px dotted #7f96d6;border-bottom:1px dotted #7f96d6;padding:4px 0}
.foot-nav li{font-size:10px;color:#b5c3ea;padding:0 12px;border-left:1px solid #5672c2}
.foot-nav li:first-child{border-left:0;color:#fff}
.copyright{left:0;top:1174px;width:760px;height:26px;background:var(--navy);color:#d7ddef;font-size:9px;display:flex;align-items:center;justify-content:center}
</style>
</head>
<body>

<nav class="top-nav abs">
  <span>HOME</span><span>ABOUT US</span><span>PRIVATE SESSIONS</span><span>CORPORATE</span><span>RETREATS</span><span>THERAPY</span><span>GALLERY</span><span>CONTACT US</span>
</nav>

<header class="hero abs">
  <div class="hero-photo abs" role="img" aria-label="Man and woman meditating cross-legged on a beach"></div>
  <div class="phone abs">
    <svg width="20" height="20" viewBox="0 0 20 20"><circle cx="10" cy="10" r="9" fill="none" stroke="#111" stroke-width="1.5"/><path d="M7 5.5l1.6 2.4-1 1.2c.6 1.3 1.5 2.2 2.8 2.8l1.2-1 2.4 1.6-.8 1.9c-3.5-.2-6.8-3.5-7-7z" fill="#111"/></svg>
    123-456-7890
  </div>
  <svg class="hero-arrow abs" style="left:8px" width="16" height="44" viewBox="0 0 16 44"><path d="M14 2L3 22l11 20" fill="none" stroke="#fff" stroke-width="2.5"/></svg>
  <svg class="hero-arrow abs" style="right:8px" width="16" height="44" viewBox="0 0 16 44"><path d="M2 2l11 20L2 42" fill="none" stroke="#fff" stroke-width="2.5"/></svg>
  <div class="brand abs"><span class="brand-dot"></span><span class="brand-name">Mirel Yoga</span></div>
  <div class="brand-tag abs">Yoga For Truth</div>
  <div class="hero-band abs"></div>
  <p class="hero-line1 abs">Consequatus autem vel eum iriure dolor in hendrerit in vulputate.</p>
  <p class="hero-line2 abs">Duis autem vel eum iriure dolor in hendrerit in vulputate velit ess.</p>
  <a class="btn-start abs">GET STARTED</a>
</header>

<section class="welcome abs">
  <h1 class="welcome-title abs"><span class="lead">WELCOME TO</span><span class="name">Mirel Yoga</span></h1>
  <div class="welcome-rule abs"></div>
  <p class="welcome-copy abs">Lorem ipsum dolor sit amet, consectetuer adipiscing elit, sed diam nonummy nibh euismod tincidunt ut laoreet dolorei magna aliquam erat volutpat. Ut wisi enim ad minim veniam, quis nostrud exerci tation ullamcorper suscipit lobortiseri nisl ut aliquip ex ea comm. odo consequat. Duis autem vel eum iriure lore eros et accumsan et iusto odio dignissim To vote blandit praesent luptatum zzril delenit augue duisolore eros et accumsan et iusto odio dignissim To vote blandit praesent luptatum zzril delenit augue duisolore in hendrerit in vulputate velit esse.molestie consequat, vel illum dolore eu feugiat nulla facilisis at vero eros et accumsan et iusto odio dignissim To vote blandit praesent luptatum zzril delenit augue duisolore uptatum zzril delenit.</p>
  <a class="btn-more abs"><span class="plus">+</span>READ MORE</a>
  <div class="video abs">
    <div class="video-frame" role="img" aria-label="Intro video still of a woman in an orange robe meditating"></div>
    <div class="video-bar">
      <svg width="8" height="8" viewBox="0 0 8 8"><path d="M1 0l7 4-7 4z" fill="#fff"/></svg>
      <span>04:59</span><div class="video-track"><span></span></div><span>10:35</span>
      <svg width="9" height="8" viewBox="0 0 9 8"><path d="M0 2.5h2L5 0v8L2 5.5H0z" fill="#fff"/></svg>
    </div>
    <svg style="position:absolute;left:108px;top:48px" width="36" height="36" viewBox="0 0 36 36"><circle cx="18" cy="18" r="17" fill="rgba(255,255,255,.7)"/><path d="M14 11l11 7-11 7z" fill="#444"/></svg>
  </div>
  <div class="video-note abs">
    <svg width="44" height="18" viewBox="0 0 44 18"><path d="M42 12C30 17 12 16 3 4" fill="none" stroke="var(--blue)" stroke-width="1.5"/><path d="M1 1l1 7 5-4z" fill="var(--blue)"/></svg>
    PLEASE WATCH INTRO VIDEO
  </div>
</section>

<section class="card blog-card abs">
  <div class="card-tab">LATEST <b>BLOG</b>
    <svg class="leaf" width="50" height="40" viewBox="0 0 50 40"><path d="M8 38C4 18 18 2 44 2c2 22-12 36-36 36z" fill="#c9d7f4"/><rect x="12" y="13" width="16" height="13" rx="2" fill="none" stroke="var(--sky)" stroke-width="2"/><path d="M16 26l-2 4 5-4" fill="var(--sky)"/></svg>
  </div>
  <div class="post" style="left:5px;top:58px;width:130px">
    <div class="t">Ut tellus dolor, dapibus</div>
    <div class="d">01.01.2015</div>
    <div class="x">Utm tellus dolor, dapibus<br>cursu eleifelitas.<em>[...]</em></div>
    <div class="share"><span>Like</span><span>Share</span></div>
  </div>
  <div class="thumb" style="left:142px;top:56px;width:82px;height:70px" role="img" aria-label="Woman holding hands in prayer"></div>
  <div class="thumb" style="left:3px;top:138px;width:82px;height:70px;background:linear-gradient(135deg,#5a2e2e,#a0463f 50%,#7d5a45)" role="img" aria-label="Children in a classroom"></div>
  <div class="post" style="left:92px;top:140px;width:130px">
    <div class="t">Ut tellus dolor, dapibus</div>
    <div class="d">01.01.2015</div>
    <div class="x">Utm tellus dolor, dapibus<br>cursu eleifelitas.<em>[...]</em></div>
    <div class="share"><span>Like</span><span>Share</span></div>
  </div>
  <div class="pager">‹›</div>
</section>

<section class="card news-card abs">
  <div class="card-tab">LATEST <b>NEWS</b>
    <svg class="leaf" width="50" height="40" viewBox="0 0 50 40"><path d="M8 38C4 18 18 2 44 2c2 22-12 36-36 36z" fill="#c9d7f4"/><path d="M10 16h6l12-6v18l-12-6h-6z" fill="var(--sky)"/></svg>
  </div>
  <div class="news-item" style="top:62px;left:-9px"><div class="news-date"><div class="n">17</div><div class="m">JUNE</div></div><div class="news-text"><strong>Lorem ipsum dolor sitak ametn</strong>Lorem ipsum dolor sitak amet, co adipiscing elit, euismod poor.</div></div>
  <div class="news-item" style="top:114px;left:-9px"><div class="news-date"><div class="n">15</div><div class="m">JUNE</div></div><div class="news-text"><strong>Lorem ipsum dolor sitak ametn</strong>Lorem ipsum dolor sitak amet, co adipiscing elit, euismod poor.</div></div>
  <div class="news-item" style="top:166px;left:-9px"><div class="news-date"><div class="n">14</div><div class="m">JUNE</div></div><div class="news-text"><strong>Lorem ipsum dolor sitak ametn</strong>Lorem ipsum dolor sitak amet, co adipiscing elit, euismod poor.</div></div>
  <div class="pager">‹›</div>
</section>

<section class="card event-card abs">
  <div class="card-tab">EVENT <b>CALANDER</b>
    <svg class="leaf" width="50" height="40" viewBox="0 0 50 40"><path d="M8 38C4 18 18 2 44 2c2 22-12 36-36 36z" fill="#c9d7f4"/><rect x="12" y="11" width="18" height="16" rx="2" fill="none" stroke="var(--sky)" stroke-width="2"/><path d="M12 16h18M16 8v5M26 8v5" stroke="var(--sky)" stroke-width="2"/></svg>
  </div>
  <div class="cal">
    <div class="cal-head"><span>FEBRUARY</span><span>2015</span></div>
    <div class="cal-grid">
      <span class="w">S</span><span class="w">M</span><span class="w">T</span><span class="w">W</span><span class="w">T</span><span class="w">F</span><span class="w">S</span>
      <span>1</span><span>2</span><span>3</span><span class="today">4</span><span>5</span><span>6</span><span>7</span>
      <span>8</span><span>9</span><span>10</span><span>11</span><span>12</span><span>13</span><span>14</span>
      <span>15</span><span>16</span><span>17</span><span>18</span><span>19</span><span>20</span><span>21</span>
      <span>22</span><span>23</span><span>24</span><span>25</span><span>26</span><span>27</span><span>28</span>
    </div>
  </div>
  <p class="cal-note">Lorem ipsum dolor sitak amet.</p>
</section>

<h2 class="gallery-title abs">IMAGE <b>GALLERY</b></h2>
<svg class="abs" style="left:150px;top:900px" width="50" height="40" viewBox="0 0 50 40"><path d="M8 38C4 18 18 2 44 2c2 22-12 36-36 36z" fill="#c9d7f4"/><rect x="11" y="14" width="14" height="11" fill="none" stroke="var(--sky)" stroke-width="2"/><rect x="15" y="10" width="14" height="11" fill="none" stroke="var(--sky)" stroke-width="2"/></svg>

<section class="film abs">
  <div class="film-holes" style="top:5px"><i></i><i></i><i></i><i></i><i></i><i></i><i></i><i></i><i></i><i></i><i></i><i></i><i></i><i></i><i></i><i></i><i></i><i></i><i></i><i></i><i></i><i></i><i></i><i></i><i></i><i></i><i></i><i></i><i></i><i></i><i></i><i></i><i></i></div>
  <div class="film-holes" style="bottom:5px"><i></i><i></i><i></i><i></i><i></i><i></i><i></i><i></i><i></i><i></i><i></i><i></i><i></i><i></i><i></i><i></i><i></i><i></i><i></i><i></i><i></i><i></i><i></i><i></i><i></i><i></i><i></i><i></i><i></i><i></i><i></i><i></i><i></i></div>
  <div class="film-arrow" style="left:4px"><svg width="17" height="17" viewBox="0 0 17 17"><path d="M10 4l-4 4.5 4 4.5" fill="none" stroke="#fff" stroke-width="2"/></svg></div>
  <div class="film-photo" style="left:40px;background:linear-gradient(160deg,#8bb3d9,#d8d2c4 60%,#b2a28c)" role="img" aria-label="Woman in a seated yoga stretch"></div>
  <div class="film-photo" style="left:200px;background:linear-gradient(160deg,#b9cf78,#6e9a3c 55%,#e4e2d6)" role="img" aria-label="Woman in a backbend pose outdoors"></div>
  <div class="film-photo" style="left:360px;background:linear-gradient(180deg,#eef1f6,#d8dde6 60%,#c9c3b8)" role="img" aria-label="Woman in white meditating"></div>
  <div class="film-photo" style="left:521px;background:linear-gradient(160deg,#7fa6cf,#b89070 55%,#6d5440)" role="img" aria-label="Woman in a yoga pose on rocks by the sea"></div>
  <div class="film-arrow" style="right:4px"><svg width="17" height="17" viewBox="0 0 17 17"><path d="M7 4l4 4.5-4 4.5" fill="none" stroke="#fff" stroke-width="2"/></svg></div>
</section>

<aside class="social abs" aria-label="Social media links"><i></i><i></i><i></i><i></i></aside>

<footer>
  <nav class="foot-nav abs">
    <ul><li>Home</li><li>About</li><li>Private Sessions</li><li>Corporate</li><li>Retreats</li><li>Therapy</li><li>Gallery</li><li>Contact Us</li></ul>
  </nav>
  <p class="copyright abs">© 2015 mirelyoga. All Rights Reserved &nbsp;|&nbsp; Terms and Conditions &nbsp;|&nbsp; Privacy Policy</p>
</footer>

</body>
</html>
```